Designing a brochures for an educational counseling service provider

We would like a 4 sided design on a 11x8.5 paper, half folded. I have including a sample design we did to give you an idea of what we envision but we welcome creativity to make beautiful looking flyers. Text for the flier is included as well as our logo.
- The most important thing is capturing our audience/market. We will be handing these flies to schools, organizations and individual clients.

www.plorvaeducationalconsultants.example

Target Market(s)

We are targeting international students wanting to study in the U.S and Canada.

Industry/Entity Type

Education

Requirements
Must have
• - Clean and clear
• - Our logo should visible and well placed.
• - Could you the pictures of students, libraries and school buildings or you could use the pictures we already have.
Nice to have
• We would like this to match business cards.

```html
<!DOCTYPE html>
<html lang="en">
<head>
<meta charset="utf-8">
<title>Plorva Educational Consultants – Brochure</title>
<link href="https://fonts.googleapis.com/css2?family=Questrial&display=swap" rel="stylesheet">
<style>
:root{
  --blue:#1f7fcf;
  --blue-deep:#1565b3;
  --green:#4fa83a;
  --green-dark:#3b8a2c;
  --orange:#ee7a12;
  --grey-light:#eef0f3;
  --ink:#262a33;
  --paper:#ffffff;
  --stage:#e6e8eb;
}
*{box-sizing:border-box;margin:0;padding:0}
html,body{width:936px;height:1200px;overflow:hidden}
body{background:var(--stage);font-family:"Questrial",sans-serif;color:var(--ink);position:relative}
.spread{position:absolute;left:98px;width:740px;height:572px;background:var(--paper);overflow:hidden;box-shadow:0 2px 10px rgba(0,0,0,.15)}
.spread--cover{top:18px}
.spread--inside{top:610px}
.spread::after{content:"";position:absolute;left:369px;top:0;width:2px;height:100%;background:linear-gradient(90deg,rgba(0,0,0,.08),rgba(0,0,0,0));pointer-events:none}
.art{position:absolute;inset:0}
.abs{position:absolute}

/* cover */
.cover-tagline{left:390px;top:34px;width:220px;color:#fff;font-size:12.5px;line-height:1.4;text-shadow:0 1px 3px rgba(0,0,0,.45)}
.cover-heading{color:var(--blue);font-size:16px;font-weight:400;letter-spacing:.2px;white-space:nowrap}
.cover-heading--back{left:24px;top:352px}
.cover-heading--front{left:396px;top:284px}
.brand{display:flex;align-items:center;gap:7px;color:var(--blue-deep);font-size:16px;letter-spacing:.5px}
.brand__dot{width:13px;height:13px;border-radius:50%;background:var(--green)}
.brand--front{right:28px;top:334px}
.brand--back{left:262px;top:500px;font-size:14px}
.brand--inside{left:22px;top:14px;color:#fff;font-size:16px}
.brand--inside .brand__dot{background:#fff}
.services{left:392px;top:440px;width:330px;display:flex;justify-content:space-between}
.service{width:76px;text-align:center;color:var(--blue);font-size:9.5px}
.service__icon{width:30px;height:30px;margin:0 auto 5px;border-radius:50%;background:var(--blue);display:flex;align-items:center;justify-content:center}
.contact{left:24px;top:418px;width:230px;font-size:9px;line-height:1.45}
.contact__tag{display:inline-block;background:var(--blue);color:#fff;font-size:9.5px;padding:2px 8px;margin-bottom:5px}
.contact__company{color:var(--blue)}
.contact__row{display:flex;align-items:center;gap:6px;margin-top:2px;white-space:nowrap}
.contact__ico{width:12px;height:12px;border-radius:50%;background:var(--blue);flex:none;display:flex;align-items:center;justify-content:center}

/* inside */
.panel{position:absolute;color:#fff;padding:16px 18px;font-size:7.2px;line-height:1.45}
.panel h2{font-size:11px;font-weight:400;margin:0 0 4px}
.panel p{margin-bottom:6px}
.panel--about{left:0;top:0;width:200px;height:280px;background:var(--orange);padding-top:46px}
.panel--services{left:160px;top:280px;width:210px;height:292px;background:var(--blue)}
.panel--schools{left:370px;top:0;width:190px;height:310px;background:var(--orange)}
.panel--transfer{left:560px;top:320px;width:180px;height:252px;background:var(--blue)}
.checklist{list-style:none;margin-top:3px}
.checklist li{padding-left:10px;position:relative;margin-bottom:1px}
.checklist li::before{content:"✓";position:absolute;left:0}
</style>
</head>
<body>

<section class="spread spread--cover">
  <svg class="art" width="740" height="572" viewBox="0 0 740 572">
    <defs>
      <linearGradient id="bandGrad" x1="0" y1="0" x2="1" y2="0">
        <stop offset="0" stop-color="#eceef1"/><stop offset="1" stop-color="#cfd2d8"/>
      </linearGradient>
      <linearGradient id="gradPhoto" x1="0" y1="0" x2="1" y2="1">
        <stop offset="0" stop-color="#98ad86"/><stop offset=".6" stop-color="#6a6d78"/><stop offset="1" stop-color="#585b66"/>
      </linearGradient>
      <linearGradient id="groupPhoto" x1="0" y1="0" x2="1" y2="1">
        <stop offset="0" stop-color="#9c857a"/><stop offset=".5" stop-color="#c9ab98"/><stop offset="1" stop-color="#dfe2e7"/>
      </linearGradient>
    </defs>
    <g role="img" aria-label="Photo of smiling graduates in caps and gowns holding diplomas">
      <polygon points="0,0 370,0 370,190 0,330" fill="url(#gradPhoto)"/>
    </g>
    <polygon points="0,330 370,190 370,198 0,338" fill="var(--blue)"/>
    <polygon points="0,338 370,198 370,300 0,400" fill="url(#bandGrad)"/>
    <g role="img" aria-label="Photo of a group of smiling students">
      <polygon points="370,0 740,0 740,262 370,205" fill="url(#groupPhoto)"/>
    </g>
    <polygon points="370,205 740,262 740,270 370,213" fill="var(--blue)"/>
    <polygon points="370,213 740,270 740,380 370,330" fill="var(--grey-light)"/>
    <polygon points="296,240 370,195 370,308" fill="var(--green-dark)"/>
    <polygon points="370,195 468,240 370,308" fill="var(--green)"/>
  </svg>

  <p class="abs cover-tagline">A full-service international educational consulting group serving students and families across the globe.</p>
  <h2 class="abs cover-heading cover-heading--back">Helping Student Fulfil the Potential</h2>
  <h1 class="abs cover-heading cover-heading--front">Preparing Studendts for Successful Future</h1>

  <div class="abs brand brand--front"><span class="brand__dot"></span>PLORVA</div>
  <div class="abs brand brand--back"><span class="brand__dot"></span>PLORVA</div>

  <div class="abs contact">
    <span class="contact__tag">Get in Touch</span>
    <div>Executive Director &amp; Independent<br>Educational Consultant</div>
    <div class="contact__company">Plorva International Educational Consultants, LLC</div>
    <div class="contact__row"><span class="contact__ico"><svg width="7" height="7" viewBox="0 0 10 10"><path d="M5 0C3 0 1.5 1.5 1.5 3.5 1.5 6 5 10 5 10s3.5-4 3.5-6.5C8.5 1.5 7 0 5 0z" fill="#fff"/></svg></span>418 Harrow Lane Suite 12B, Elmsford, TX 75010</div>
    <div class="contact__row"><span class="contact__ico"><svg width="7" height="7" viewBox="0 0 10 10"><path d="M2 0l2 2.5-1.2 1.3a6 6 0 003.4 3.4L7.5 6 10 8l-1.5 2C4 10 0 6 0 1.5z" fill="#fff"/></svg></span>555-013-2846</div>
    <div class="contact__row"><span class="contact__ico"><svg width="7" height="6" viewBox="0 0 10 8"><rect width="10" height="8" fill="#fff"/><path d="M0 0l5 4 5-4" stroke="#1f7fcf" fill="none"/></svg></span>nadia@plorvaeducationalconsultants.example</div>
    <div class="contact__row"><span class="contact__ico"><svg width="7" height="7" viewBox="0 0 10 10"><circle cx="5" cy="5" r="4" stroke="#fff" fill="none"/><path d="M1 5h8M5 1c-2 2-2 6 0 8M5 1c2 2 2 6 0 8" stroke="#fff" fill="none"/></svg></span>www.plorvaeducationalconsultants.example</div>
  </div>

  <div class="abs services">
    <div class="service"><div class="service__icon"><svg width="14" height="14" viewBox="0 0 14 14"><path d="M7 1L1 4h12zM2 5h10v1H2zM3 6h1.5v5H3zM6.25 6h1.5v5h-1.5zM9.5 6H11v5H9.5zM1 11.5h12V13H1z" fill="#fff"/></svg></div>Boarding School</div>
    <div class="service"><div class="service__icon"><svg width="14" height="14" viewBox="0 0 14 14"><rect x="2" y="2" width="8" height="10" fill="none" stroke="#fff"/><path d="M12 2l-5 6-1 2 2-1 5-6z" fill="#fff"/></svg></div>College Admission</div>
    <div class="service"><div class="service__icon"><svg width="14" height="14" viewBox="0 0 14 14"><path d="M2 5h8l-2-2M12 9H4l2 2" stroke="#fff" fill="none" stroke-width="1.4"/></svg></div>Transfer Students</div>
    <div class="service"><div class="service__icon"><svg width="16" height="14" viewBox="0 0 16 14"><path d="M8 2L1 5l7 3 7-3z" fill="#fff"/><path d="M4 7v3c2 2 6 2 8 0V7L8 9z" fill="#fff"/></svg></div>Graduate Students</div>
  </div>
</section>

<section class="spread spread--inside">
  <svg class="art" width="740" height="572" viewBox="0 0 740 572">
    <defs>
      <linearGradient id="grassPhoto" x1="0" y1="0" x2="0" y2="1">
        <stop offset="0" stop-color="#9cc46a"/><stop offset="1" stop-color="#7fa955"/>
      </linearGradient>
      <linearGradient id="benchPhoto" x1="0" y1="0" x2="1" y2="1">
        <stop offset="0" stop-color="#cfdcae"/><stop offset="1" stop-color="#a08a70"/>
      </linearGradient>
      <linearGradient id="courtPhoto" x1="0" y1="0" x2="0" y2="1">
        <stop offset="0" stop-color="#b3d0ec"/><stop offset="1" stop-color="#6f95c3"/>
      </linearGradient>
      <linearGradient id="capsPhoto" x1="0" y1="0" x2="0" y2="1">
        <stop offset="0" stop-color="#d6dae0"/><stop offset="1" stop-color="#7c808b"/>
      </linearGradient>
    </defs>
    <rect x="200" y="0" width="170" height="280" fill="url(#grassPhoto)" role="img" aria-label="Photo of students studying together on a lawn"/>
    <rect x="0" y="280" width="160" height="292" fill="url(#benchPhoto)" role="img" aria-label="Photo of a diverse group of students sitting outdoors with laptops"/>
    <rect x="560" y="0" width="180" height="320" fill="url(#courtPhoto)" role="img" aria-label="Photo of students playing basketball"/>
    <rect x="370" y="310" width="190" height="262" fill="url(#capsPhoto)" role="img" aria-label="Photo of graduates in caps and gowns"/>
  </svg>

  <div class="abs brand brand--inside"><span class="brand__dot"></span>PLORVA</div>

  <div class="panel panel--about">
    <h2>About Us:</h2>
    <p>Our mission is to make quality education accessible and affordable to the families we serve. Our services are designed with the child's future in mind, whether one is seeking an academic or non-academic setting, it is important to us that we set our clients up for success.</p>
    <p>We are a family-centered organization and our goals are the same as those of our clients: for their child to grow and reach their goals and dreams. With years of experience in the field, we know the obstacles parents face. Our consultants work closely with families to find affordable and quality educational options.</p>
  </div>

  <div class="panel panel--services">
    <h2>Services:</h2>
    <p>Finding the right school or program for your child is one of the most important decisions your family will make. The right choice will make a major impact on your child's future.</p>
    <p>Our package includes:</p>
    <ul class="checklist">
      <li>Intake interview</li>
      <li>Present range of options based on needs and goals of the family</li>
      <li>Interview coaching</li>
      <li>Assistance with application and essays</li>
      <li>Updates on student progress throughout the enrollment with the school</li>
      <li>Advisement on financial documents and visa applications</li>
    </ul>
  </div>

  <div class="panel panel--schools">
    <h2>Boarding schools:</h2>
    <p>Students who want the best out of their grade school years often choose boarding schools. These schools offer small classes, strong guidance and a rich campus life that helps students build independence and prepare for college.</p>
    <h2>College admission:</h2>
    <p>Our consultants specialize in the college admission process and understand how stressful it can be. We guide families step by step, from building a school list to essays, interviews and final decisions, so students apply with confidence.</p>
    <p>Clients increase the odds of admission with our personal attention and planning, and many are accepted to their first choice.</p>
  </div>

  <div class="panel panel--transfer">
    <h2>Transfer students:</h2>
    <p>Need to find a school or an alternative school that is a better match for your child? We work with students and families to transfer from one school to another.</p>
    <h2>Scholarships:</h2>
    <p>Funding the education for your children in some of the world's top schools can be very expensive. We work with you to determine the budget for your family and guide you through the financial aid process.</p>
    <p>Over 70% of our clients have been awarded scholarships or financial aid, making your child's education affordable and possible.</p>
  </div>
</section>

</body>
</html>
```